" Empresa focada em seguros pessoais, tais como seguro saúde, vida, previdência e odontológico, oferecendo segurança e agilidade na contrataçao e manutençao e também qualidade de vida. "

```html
<!DOCTYPE html>
<html lang="pt-BR">
<head>
<meta charset="UTF-8">
<title>Celestia — Cartão de Visita</title>
<link rel="stylesheet" href="https://fonts.googleapis.com/css2?family=Arimo:wght@400;700&display=swap">
<style>
  :root {
    --navy: #1f3f8f;
    --teal: #31c0d3;
    --white: #ffffff;
    --grey: #5d6670;
    --backdrop: #e9e6e2;
  }
  * { box-sizing: border-box; margin: 0; padding: 0; }
  html, body {
    width: 1200px; height: 1200px; overflow: hidden;
    background: var(--backdrop);
    font-family: "Arimo", Arial, sans-serif;
  }
  .sheet {
    width: 1200px; height: 1200px;
    display: flex; flex-direction: column; align-items: center; justify-content: center;
    gap: 60px;
  }
  .card {
    position: relative;
    width: 900px; height: 500px;
    background: var(--white);
    overflow: hidden;
    box-shadow: 0 6px 20px rgba(0,0,0,0.12);
  }

  /* Front */
  .brand {
    position: absolute; left: 0; right: 0; top: 150px;
    display: flex; align-items: center; justify-content: center; gap: 26px;
  }
  .brand-dot {
    width: 72px; height: 72px; border-radius: 50%;
    background: var(--teal);
  }
  .brand-text { display: flex; flex-direction: column; }
  .brand-name {
    font-size: 78px; font-weight: 400; color: var(--navy);
    line-height: 1; letter-spacing: -1px;
  }
  .brand-tagline {
    font-size: 22px; color: var(--teal); letter-spacing: 1.5px; margin-top: 6px;
  }
  .band { position: absolute; height: 22px; }
  .band-navy {
    left: 0; width: 420px; top: 360px;
    background: var(--navy); border-radius: 0 11px 11px 0;
  }
  .band-teal {
    right: 0; width: 370px; top: 410px;
    background: var(--teal); border-radius: 11px 0 0 11px;
  }
  .web {
    position: absolute; left: 300px; top: 398px;
    font-size: 22px; color: var(--navy); letter-spacing: 0.5px;
  }

  /* Back */
  .panel {
    position: absolute; left: 0; top: 0; bottom: 0; width: 270px;
    background: var(--teal);
  }
  .contact {
    position: absolute; right: 90px; top: 130px;
    text-align: right;
  }
  .person-name { font-size: 34px; font-weight: 700; color: var(--navy); }
  .person-role { font-size: 22px; color: var(--grey); margin-top: 6px; }
  .contact-lines {
    list-style: none; margin-top: 70px;
    font-size: 23px; line-height: 1.38; color: var(--navy);
  }
  .edge-bar {
    position: absolute; right: 0; top: 215px; width: 22px; height: 160px;
    background: var(--navy); border-radius: 11px 0 0 11px;
  }
</style>
</head>
<body>
  <main class="sheet">
    <section class="card card-front" aria-label="Frente do cartão">
      <div class="brand">
        <span class="brand-dot"></span>
        <div class="brand-text">
          <span class="brand-name">Celestia</span>
          <span class="brand-tagline">Consultoria de Benefícios</span>
        </div>
      </div>
      <span class="band band-navy"></span>
      <span class="web">www.celestia.com.br</span>
      <span class="band band-teal"></span>
    </section>

    <section class="card card-back" aria-label="Verso do cartão">
      <div class="panel"></div>
      <div class="contact">
        <p class="person-name">Nome Sobrenome</p>
        <p class="person-role">Cargo</p>
        <ul class="contact-lines">
          <li>Av. Celestia, 00</li>
          <li>(11) 0000-0000</li>
          <li>(11) 0000-0000</li>
          <li>contato@celestia.com.br</li>
        </ul>
      </div>
      <span class="edge-bar"></span>
    </section>
  </main>
</body>
</html>
```